Cutting edge GUI for a conventional C# Forms Project

I have an existing C# Forms application. The current GUI design format is Win 95 style forms. I would like to elevate the look of the software.

There are a total of six forms. Apart from two forms at 1024 X 600, the others are of different sizes. I am open to resizing them depending on the design.

I am attaching the user manual of the product to give you a better idea of what the application does. The manual also contains screenshots of individual screens. I am open to sharing the C# source files if needed.

Target Market(s)

Industrial application - Field Representatives - Will be used in Outdoor environments.

Industry/Entity Type

Software

Requirements
Must have
• A very cool, futuristic design.
Design should be light-weight as the application maybe run on net-books and low end tablets.
Should not have
• Redundant point but keep in mind that this design is going to be used in a software. So light weight is highly appreciated.

```html
<!DOCTYPE html>
<html lang="en">
<head>
<meta charset="utf-8">
<title>Field Console UI Kit</title>
<link href="https://fonts.googleapis.com/css2?family=Open+Sans:wght@400;600;700&display=swap" rel="stylesheet">
<style>
:root{
  --bg:#2a2a2c;
  --frame:#323234;
  --frame-edge:#1c1c1e;
  --blue-top:#4aa3ee;
  --blue-bot:#1560b8;
  --blue-glow:rgba(70,150,230,.45);
  --green-top:#5fd03e;
  --green-bot:#2a9a17;
  --green-glow:rgba(90,200,60,.35);
  --grey-top:#8a8a8c;
  --grey-bot:#4a4a4c;
  --pill-dark-top:#4a4a4c;
  --pill-dark-bot:#2c2c2e;
  --pill-blue-top:#2f86dd;
  --pill-blue-bot:#0f4fa3;
  --pill-green-top:#2fb52a;
  --pill-green-bot:#0f7c12;
  --text:#ffffff;
  --accent:#1fa6ff;
}
*{box-sizing:border-box;margin:0;padding:0}
html,body{width:1200px;height:1200px;overflow:hidden;background:var(--bg)}
body{position:relative;font-family:"Open Sans",Arial,sans-serif;color:var(--text)}
.icon-defs{position:absolute;width:0;height:0}

.tile{position:absolute;width:202px;height:193px;border-radius:9px;
  background:linear-gradient(#3a3a3c,#262628);
  border:1px solid #4a4a4c;box-shadow:0 2px 4px rgba(0,0,0,.6)}
.tile-face{position:absolute;left:12px;top:12px;right:12px;bottom:12px;border-radius:4px;
  border:1px solid rgba(0,0,0,.5);display:flex;flex-direction:column;align-items:center;
  box-shadow:inset 0 1px 0 rgba(255,255,255,.35),inset 0 0 12px rgba(0,0,0,.35)}
.tile-face svg{width:86px;height:86px;margin-top:20px;color:#fff;filter:drop-shadow(0 1px 1px rgba(0,0,0,.5))}
.tile-label{font-weight:600;font-size:21px;letter-spacing:.2px;margin-top:6px;text-shadow:0 1px 2px rgba(0,0,0,.6)}
.tile--blue{box-shadow:0 0 14px var(--blue-glow),0 2px 4px rgba(0,0,0,.6)}
.tile--blue .tile-face{background:linear-gradient(var(--blue-top),var(--blue-bot))}
.tile--green{box-shadow:0 0 14px var(--green-glow),0 2px 4px rgba(0,0,0,.6)}
.tile--green .tile-face{background:linear-gradient(var(--green-top),var(--green-bot))}
.tile--grey .tile-face{background:radial-gradient(ellipse at 50% 45%,var(--grey-top),var(--grey-bot))}

.pill{position:absolute;height:46px;border-radius:23px;display:flex;align-items:center;justify-content:center;
  gap:10px;font-size:15px;font-weight:700;box-shadow:0 0 0 4px #1e1e20,0 3px 5px rgba(0,0,0,.6);
  border:1px solid rgba(255,255,255,.15)}
.pill--dark{background:linear-gradient(var(--pill-dark-top),var(--pill-dark-bot))}
.pill--blue{background:linear-gradient(var(--pill-blue-top),var(--pill-blue-bot))}
.pill--green{background:linear-gradient(var(--pill-green-top),var(--pill-green-bot))}
.pill-check{width:16px;height:16px;background:#9a9aa4;border:2px solid #d8d8de}

.section-list{position:absolute;left:48px;top:1075px;width:272px}
.section-item{height:42px;line-height:42px;padding-left:18px;font-size:14px}
.section-item--idle{background:#363444;color:#d8d8e0;border:1px solid #47455a}
.section-item--active{background:#d8d8d8;color:#333}

.checkbox{position:absolute;width:19px;height:19px;left:354px;border:1px solid #555568}
.checkbox--off{top:1089px;background:#3a3a50}
.checkbox--on{top:1127px;background:#2c3240}
.checkbox--on svg{width:17px;height:17px}
.radio{position:absolute;left:402px;width:14px;height:14px;border-radius:50%;background:#34343c;border:1px solid #4a4a55}
.radio::after{content:"";position:absolute;left:3px;top:3px;width:6px;height:6px;border-radius:50%}
.radio--off{top:1094px}.radio--off::after{background:#9a9aa8}
.radio--on{top:1132px}.radio--on::after{background:var(--accent);box-shadow:0 0 4px var(--accent)}
</style>
</head>
<body>
<svg class="icon-defs" aria-hidden="true">
  <symbol id="i-rocket" viewBox="0 0 64 64">
    <path fill="currentColor" d="M60 4C46 5 34 12 26 24l-6 2-6 8 8 1 7 7 1 8 8-6 2-6c12-8 19-20 20-34zM44 14a5 5 0 1 1 0 .1z"/>
    <path fill="none" stroke="currentColor" stroke-width="3" stroke-linecap="round" d="M20 40 6 54M14 34 4 44M28 46 18 56"/>
  </symbol>
  <symbol id="i-cloud" viewBox="0 0 64 64">
    <path fill="currentColor" d="M18 48a12 12 0 0 1-1-24 16 16 0 0 1 30-4 12 12 0 0 1 2 28z"/>
    <path fill="#1560b8" d="M27 22h10v12h7L32 46 20 34h7z" opacity=".9"/>
    <path fill="none" stroke="currentColor" stroke-width="3" d="M36 50l10-10"/>
  </symbol>
  <symbol id="i-board" viewBox="0 0 64 64">
    <path fill="currentColor" d="M32 4l3 6h-6z"/>
    <rect x="12" y="10" width="40" height="32" rx="2" fill="currentColor"/>
    <g fill="#222"><rect x="18" y="16" width="4" height="3"/><rect x="24" y="16" width="22" height="3"/><rect x="18" y="22" width="4" height="3"/><rect x="24" y="22" width="22" height="3"/><rect x="18" y="28" width="4" height="3"/><rect x="24" y="28" width="22" height="3"/><rect x="18" y="34" width="4" height="3"/><rect x="24" y="34" width="22" height="3"/></g>
    <path stroke="currentColor" stroke-width="3" d="M22 42l-6 16M42 42l6 16M32 42v10"/>
  </symbol>
  <symbol id="i-clip" viewBox="0 0 64 64">
    <rect x="14" y="10" width="36" height="48" rx="2" fill="none" stroke="currentColor" stroke-width="4"/>
    <rect x="24" y="6" width="16" height="10" rx="2" fill="currentColor"/>
    <circle cx="32" cy="9" r="2" fill="#222"/>
    <path fill="none" stroke="currentColor" stroke-width="3" stroke-linejoin="round" d="M18 36h8l3-8 5 16 4-10h8"/>
  </symbol>
</svg>

<!-- Blue tiles -->
<div class="tile tile--blue" style="left:48px;top:48px"><div class="tile-face"><svg><use href="#i-rocket"/></svg><span class="tile-label">LAUNCH</span></div></div>
<div class="tile tile--blue" style="left:342px;top:48px"><div class="tile-face"><svg><use href="#i-cloud"/></svg><span class="tile-label">DOWNLOAD</span></div></div>
<div class="tile tile--blue" style="left:647px;top:48px"><div class="tile-face"><svg><use href="#i-board"/></svg><span class="tile-label">VIEW RUNS</span></div></div>
<div class="tile tile--blue" style="left:936px;top:48px"><div class="tile-face"><svg><use href="#i-clip"/></svg><span class="tile-label">DIAGNOSTICS</span></div></div>

<!-- Green tiles -->
<div class="tile tile--green" style="left:48px;top:287px"><div class="tile-face"><svg><use href="#i-rocket"/></svg><span class="tile-label">LAUNCH</span></div></div>
<div class="tile tile--green" style="left:342px;top:287px"><div class="tile-face"><svg><use href="#i-cloud"/></svg><span class="tile-label">DOWNLOAD</span></div></div>
<div class="tile tile--green" style="left:647px;top:287px"><div class="tile-face"><svg><use href="#i-board"/></svg><span class="tile-label">VIEW RUNS</span></div></div>
<div class="tile tile--green" style="left:936px;top:287px"><div class="tile-face"><svg><use href="#i-clip"/></svg><span class="tile-label">DIAGNOSTICS</span></div></div>

<!-- Grey tiles -->
<div class="tile tile--grey" style="left:48px;top:524px"><div class="tile-face"><svg><use href="#i-rocket"/></svg><span class="tile-label">LAUNCH</span></div></div>
<div class="tile tile--grey" style="left:342px;top:524px"><div class="tile-face"><svg><use href="#i-cloud"/></svg><span class="tile-label">DOWNLOAD</span></div></div>
<div class="tile tile--grey" style="left:647px;top:524px"><div class="tile-face"><svg><use href="#i-board"/></svg><span class="tile-label">VIEW RUNS</span></div></div>
<div class="tile tile--grey" style="left:936px;top:524px"><div class="tile-face"><svg><use href="#i-clip"/></svg><span class="tile-label">DIAGNOSTICS</span></div></div>

<!-- Dark pills -->
<div class="pill pill--dark" style="left:45px;top:776px;width:144px">&lt;&nbsp; Main Menu</div>
<div class="pill pill--dark" style="left:222px;top:776px;width:204px">Torn OFF Sensor Check</div>
<div class="pill pill--dark" style="left:452px;top:776px;width:173px">ODOMETER <span class="pill-check"></span></div>
<div class="pill pill--dark" style="left:650px;top:776px;width:147px">&lt;&nbsp; Prev Run</div>
<div class="pill pill--dark" style="left:818px;top:776px;width:171px">Create Report</div>
<div class="pill pill--dark" style="left:1019px;top:776px;width:146px">Next Run &gt;</div>

<!-- Blue pills -->
<div class="pill pill--blue" style="left:45px;top:865px;width:144px">&lt;&nbsp; Main Menu</div>
<div class="pill pill--blue" style="left:222px;top:865px;width:204px">Torn OFF Sensor Check</div>
<div class="pill pill--blue" style="left:452px;top:865px;width:173px">ODOMETER <span class="pill-check"></span></div>
<div class="pill pill--blue" style="left:650px;top:865px;width:147px">&lt;&nbsp; Prev Run</div>
<div class="pill pill--blue" style="left:818px;top:865px;width:171px">Create Report</div>
<div class="pill pill--blue" style="left:1019px;top:865px;width:146px">Next Run &gt;</div>

<!-- Green pills -->
<div class="pill pill--green" style="left:45px;top:954px;width:144px">&lt;&nbsp; Main Menu</div>
<div class="pill pill--green" style="left:222px;top:954px;width:204px">Torn OFF Sensor Check</div>
<div class="pill pill--green" style="left:452px;top:954px;width:173px">ODOMETER <span class="pill-check"></span></div>
<div class="pill pill--green" style="left:650px;top:954px;width:147px">&lt;&nbsp; Prev Run</div>
<div class="pill pill--green" style="left:818px;top:954px;width:171px">Create Report</div>
<div class="pill pill--green" style="left:1019px;top:954px;width:146px">Next Run &gt;</div>

<!-- Section list -->
<div class="section-list">
  <div class="section-item section-item--idle">Section Name</div>
  <div class="section-item section-item--active">Section Name</div>
</div>

<!-- Form controls -->
<div class="checkbox checkbox--off"></div>
<div class="checkbox checkbox--on"><svg viewBox="0 0 16 16"><path d="M3 8l3 3 7-7" fill="none" stroke="#fff" stroke-width="2"/></svg></div>
<div class="radio radio--off"></div>
<div class="radio radio--on"></div>
</body>
</html>
```